Korvane 24/7 Gym & Health Bar Webpage

We need a professional and interactive webpage for a 24/7 health club.
Our approach is professional yet friendly offering holitic professional services for both general and special populations, along with flexible 24/7 gym and group fitness memberships. Professional services that we offer;
Exercise Physiologist
Strength & Conditioning
Physiotherapy
Chiropractor
Nutrition
Personal Training
we also service acute and chronic injuries, work cover, and veteran affairs

We also have a well-being bar offers healthy food, beverages and wide range of supplements.
We send out regular newsletters and want it to be interactive with social media and e-commerce.
Final design should demonstrate a holistic approach where clients have access to a wide range of health services within a professional health club environment. needs to be phone and table friendly please

i have attached a template i had been working on but wasn't happy with it

Target Market(s)

wide demographic including:

Special population - older demographic looking for professional services. Doctors will be referring clients to us also

24/7 gym - aged 25+ yrs, male and female

Industry/Entity Type

Health And Wellness

Coding

Coded - Design and coding required

Number of Pages Required

5+ page

Colors
33a6d7
add136
ffffff
0355a3

Requirements
Must have
• atmosphere and professionalism whilst inviting and sincere
• social media interaction & blog page
• clear navigation
• mobile and table friendly
• Brisk E-newsletter sign up
• testimonials
Nice to have
• customer feedback option
• FAQ
• opportunity to integrate online shop
• ability to download free visit pass

```html
<!DOCTYPE html>
<html lang="en">
<head>
<meta charset="utf-8">
<title>Korvane 24/7 Gym &amp; Health Bar</title>
<link href="https://fonts.googleapis.com/css2?family=Raleway:ital,wght@0,400;0,500;0,600;0,700;0,800;1,400;1,600&display=swap" rel="stylesheet">
<style>
:root{
  --navy:#1d3f8c;
  --blue:#0355a3;
  --sky:#33a6d7;
  --green:#6dbe2f;
  --ink:#4a4a4a;
  --muted:#8a8a8a;
  --panel:#f4f4f4;
  --line:#e6e6e6;
  --footer:#4b4b4b;
  --white:#ffffff;
}
*{box-sizing:border-box;margin:0;padding:0}
html,body{width:676px;height:1200px;overflow:hidden;background:var(--white)}
body{position:relative;font-family:"Raleway",sans-serif;color:var(--ink)}
.abs{position:absolute}

/* header */
.site-header{position:absolute;left:0;top:0;width:676px;height:64px;background:var(--white);box-shadow:0 1px 3px rgba(0,0,0,.12);z-index:2}
.brand{position:absolute;left:56px;top:17px;display:flex;align-items:center;gap:7px}
.brand-mark{width:30px;height:30px;background:var(--blue);border-radius:50%}
.brand-name{font-size:25px;font-weight:700;color:var(--blue);letter-spacing:.5px;line-height:1}
.main-nav{position:absolute;top:29px;left:0;font-size:7px;letter-spacing:.3px;color:#777}
.main-nav a{position:absolute;white-space:nowrap;color:inherit;text-decoration:none}
.main-nav a.active{color:var(--navy);font-weight:700}

/* hero */
.hero{position:absolute;left:0;top:64px;width:676px;height:306px;
  background:linear-gradient(90deg,#8fc6e4 0%,#a9d6ee 45%,#d7c2b0 70%,#e4c9b6 85%,#bcd6e6 100%)}
.hero-kicker{left:58px;top:92px;font-size:19px;font-weight:800;color:var(--white);letter-spacing:1px}
.hero-title{left:58px;top:115px;font-size:34px;font-weight:800;color:var(--white);letter-spacing:1px}
.hero-text{left:57px;top:164px;width:280px;font-size:8.6px;line-height:13px;color:var(--white)}
.hero-offer{left:56px;top:207px;font-size:14px;font-weight:600;color:var(--white);letter-spacing:.3px}
.hero-arrow{top:136px}
.feature-tabs{position:absolute;left:56px;top:349px;width:564px;height:29px;display:flex}
.feature-tabs a{flex:1;display:flex;align-items:center;justify-content:center;color:var(--white);font-size:11px;font-weight:500;text-decoration:none}
.tab-offers{background:var(--navy)}
.tab-cafe{background:var(--green)}
.tab-services{background:var(--sky)}

/* intro */
.intro-title{left:0;width:676px;top:406px;text-align:center;font-size:14px;font-weight:600;color:#555}
.intro-text{left:88px;width:500px;top:434px;text-align:center;font-size:6.6px;line-height:11.6px;color:#666;white-space:nowrap}
.pass-btn{position:absolute;left:254px;top:483px;width:168px;height:27px;background:var(--navy);display:flex;text-decoration:none}
.pass-btn .icon{width:24px;height:27px;background:var(--green);display:flex;align-items:center;justify-content:center}
.pass-btn .label{flex:1;display:flex;align-items:center;justify-content:center;color:var(--white);font-size:8.4px;font-weight:600;letter-spacing:.2px}

/* blog */
.blog-band{position:absolute;left:0;top:540px;width:676px;height:476px;background:var(--panel)}
.section-title{font-size:13.5px;font-weight:600;color:#555}
.blog-title{left:56px;top:574px}
.blog-arrows{left:573px;top:572px}
.blog-card{position:absolute;top:615px;width:175px;height:203px;background:var(--white);border:1px solid var(--line)}
.blog-card .thumb{height:110px}
.thumb-1{background:linear-gradient(135deg,#c9a27a,#e8c9a0 50%,#9c8a7e)}
.thumb-2{background:linear-gradient(135deg,#b8b3ad,#d9d4cf 50%,#a6a09b)}
.thumb-3{background:linear-gradient(135deg,#8fb6c4,#c5d7dc 50%,#a4c98f)}
.blog-card h3{position:absolute;left:10px;top:120px;font-size:9.6px;font-weight:600;color:var(--navy)}
.blog-card p{position:absolute;left:12px;top:140px;width:155px;font-size:6.4px;line-height:11.5px;color:#888}
.blog-meta{position:absolute;left:12px;top:180px;font-size:5.3px;font-style:italic;color:#b0b0b0;display:flex;align-items:center;gap:4px}
.blog-meta .sep{width:1px;height:7px;background:#ddd;margin:0 8px}

/* newsletter + testimonials */
.box{position:absolute;top:846px;height:141px;background:var(--white);border:1px solid var(--line)}
.newsletter{left:56px;width:175px}
.newsletter h2{position:absolute;left:15px;top:18px;font-size:13px;font-weight:600;color:#555;white-space:nowrap}
.field{position:absolute;left:15px;width:140px;height:21px;background:#f2f2f2;border:1px solid #e8e8e8;font-size:6.4px;font-style:italic;color:#999;padding:6px 8px}
.subscribe-btn{position:absolute;left:16px;top:101px;width:84px;height:25px;background:var(--green);color:var(--white);font-size:10px;font-weight:600;display:flex;align-items:center;justify-content:center;letter-spacing:.3px}
.testimonials{left:250px;width:370px}
.client-photo{position:absolute;left:8px;top:16px;width:94px;height:104px;background:linear-gradient(180deg,#f4f4f4,#d9d2cc 60%,#3a3a3a)}
.testimonials h2{position:absolute;left:107px;top:20px;font-size:13px;font-weight:600;color:#555}
.quote{position:absolute;left:110px;top:55px;width:240px;font-size:6.4px;line-height:11.5px;font-style:italic;color:#777}
.client-name{position:absolute;left:108px;top:111px;font-size:7.4px;font-weight:600;color:var(--navy)}
.dots{position:absolute;left:340px;top:106px;display:flex;gap:2px}
.dots i{width:5px;height:5px;border-radius:50%;background:#ccc}
.dots i.on{background:var(--sky)}

/* footer */
.site-footer{position:absolute;left:0;top:1016px;width:676px;height:184px;background:var(--footer);color:#cfcfcf}
.foot-col{position:absolute;top:28px}
.foot-col h4{font-size:8.6px;font-weight:600;color:var(--white);letter-spacing:.2px;margin-bottom:8px;white-space:nowrap}
.foot-col li{list-style:none;font-size:6.8px;line-height:14px;white-space:nowrap}
.follow{position:absolute;left:512px;top:90px;font-size:8.6px;font-weight:600;color:var(--white)}
.socials{position:absolute;left:510px;top:106px;display:flex;gap:4px}
.socials span{width:22px;height:22px;border-radius:50%}
.s1{background:#29c5f0}.s2{background:#c4262e}.s3{background:#1d8bd8}.s4{background:#0e5f9a}
.copyright{position:absolute;left:0;width:676px;top:158px;text-align:center;font-size:5.8px;color:#ddd;word-spacing:2px}
</style>
</head>
<body>

<header class="site-header">
  <div class="brand">
    <span class="brand-mark"></span>
    <span class="brand-name">Korvane</span>
  </div>
  <nav class="main-nav">
    <a class="active" style="left:296px">HOME</a>
    <a style="left:337px">ABOUT</a>
    <a style="left:382px">SERVICES</a>
    <a style="left:437px">EVENTS</a>
    <a style="left:485px">SHOP</a>
    <a style="left:524px">CONTACT US</a>
    <a style="left:589px">CLASSES</a>
  </nav>
</header>

<section class="hero" role="img" aria-label="Photo of a runner wearing a heart-rate strap and sports watch on a beach">
  <div class="abs hero-kicker">KORVANE</div>
  <div class="abs hero-title">YOUR HEALTH</div>
  <p class="abs hero-text">Korvane was established in 2005 to offer individuals and groups quality health and fitness services in the Harbour Shire.</p>
  <div class="abs hero-offer">GET TODAY SPECIAL OFFERS</div>
  <svg class="abs hero-arrow" style="left:12px" width="22" height="38" viewBox="0 0 22 38"><polyline points="20,1 2,19 20,37" fill="none" stroke="#fff" stroke-width="1.6"/></svg>
  <svg class="abs hero-arrow" style="left:640px" width="22" height="38" viewBox="0 0 22 38"><polyline points="2,1 20,19 2,37" fill="none" stroke="#fff" stroke-width="1.6"/></svg>
</section>

<nav class="feature-tabs">
  <a class="tab-offers">Special Offers</a>
  <a class="tab-cafe">Korvane Cafe</a>
  <a class="tab-services">Features &amp; Services</a>
</nav>

<h1 class="abs intro-title">Korvane your Health and Fitness Today</h1>
<p class="abs intro-text">Korvane was established in 2005 to offer individuals and groups quality health and fitness services in the Harbour Shire.<br>Since then we have been growing and have now in 2012 moved to new bigger premises in Wrenfield where we now offer<br>new services alongside our proven solutions based personal training system.</p>
<a class="pass-btn">
  <span class="icon"><svg width="10" height="10" viewBox="0 0 10 10"><path d="M5 1v5M2.5 4L5 6.5 7.5 4M1.5 8.5h7" fill="none" stroke="#fff" stroke-width="1.4"/></svg></span>
  <span class="label">DOWNLOAD FREE VISIT PASS</span>
</a>

<section class="blog-band"></section>
<h2 class="abs section-title blog-title">Korvane Latest Blog News</h2>
<svg class="abs blog-arrows" width="50" height="22" viewBox="0 0 50 22">
  <circle cx="11" cy="11" r="10" fill="none" stroke="#ddd"/><polyline points="13,7 9,11 13,15" fill="none" stroke="#bbb"/>
  <circle cx="36" cy="11" r="10" fill="none" stroke="#ddd"/><polyline points="34,7 38,11 34,15" fill="none" stroke="#bbb"/>
</svg>

<article class="blog-card" style="left:56px">
  <div class="thumb thumb-1" role="img" aria-label="Photo of a woman jogging at sunset"></div>
  <h3>Blog Name</h3>
  <p>Korvane was established in 2005 to offer individuals and groups quality health.</p>
  <div class="blog-meta">June 18, 2015<span class="sep"></span>No comments</div>
</article>
<article class="blog-card" style="left:250px">
  <div class="thumb thumb-2" role="img" aria-label="Photo of a group fitness class doing lunges"></div>
  <h3>Blog Name</h3>
  <p>Korvane was established in 2005 to offer individuals and groups quality health.</p>
  <div class="blog-meta">June 18, 2015<span class="sep"></span>No comments</div>
</article>
<article class="blog-card" style="left:444px">
  <div class="thumb thumb-3" role="img" aria-label="Photo of people stretching on exercise mats"></div>
  <h3>Blog Name</h3>
  <p>Korvane was established in 2005 to offer individuals and groups quality health.</p>
  <div class="blog-meta">June 18, 2015<span class="sep"></span>No comments</div>
</article>

<section class="box newsletter">
  <h2>Subscribe Newsletter</h2>
  <div class="field" style="top:43px">Name:</div>
  <div class="field" style="top:72px">Email Adress</div>
  <div class="subscribe-btn">SUBSCRIBE</div>
</section>

<section class="box testimonials">
  <div class="client-photo" role="img" aria-label="Photo of two smiling clients in gym wear"></div>
  <h2>Client Testimonials</h2>
  <p class="quote">"Sed ut perspiciatis unde omnis iste natus error sit voluptatemcus antium doloremque laudantium, totam rem aperiam, eaque ipsaab illo inventore veritatis et quasi architecto beatae vitae dicta sunt explicabo. Nemo enim ipsam voluptatem quia voluptas sit a</p>
  <div class="client-name">Jhon Smith, City Name</div>
  <div class="dots"><i></i><i></i><i class="on"></i></div>
</section>

<footer class="site-footer">
  <div class="foot-col" style="left:56px">
    <h4>JOIN KORVANE</h4>
    <ul><li>Find Us</li><li>Products / Services</li><li>Free Trial</li><li>Korvane Kids / Teens Program</li><li>Social Events</li><li>Blog</li></ul>
  </div>
  <div class="foot-col" style="left:205px">
    <h4>COMPANY</h4>
    <ul><li>About Us</li><li>Careers</li><li>Contact</li><li>Terms and Conditions</li><li>Privacy Policy</li><li>FAQ</li></ul>
  </div>
  <div class="foot-col" style="left:346px">
    <h4>HEALTH &amp; FITNESS</h4>
    <ul><li>Classes / Timetable</li><li>Membership Package</li><li>Personal Training Package</li><li>Coporate Wellness</li><li>Services</li><li>Shop</li></ul>
  </div>
  <div class="foot-col" style="left:512px">
    <h4>CAFE / REFUEL STATION</h4>
    <ul><li>Products / Services</li><li>Specials</li></ul>
  </div>
  <div class="follow">FOLLOW US</div>
  <div class="socials"><span class="s1"></span><span class="s2"></span><span class="s3"></span><span class="s4"></span></div>
  <div class="copyright">Copyright © 2015 -&nbsp;&nbsp; Home&nbsp; About Us&nbsp; Schedule&nbsp; Our Blog&nbsp; Contact</div>
</footer>

</body>
</html>
```